Well Designed, Impactful Business Card

I need a new business card designed that incorporates our company colors, looks very well designed, and is of the highest quality as that reflects the work we do as a professional services firm.

We would like it to incorporate a QR code and will link to an article we have written as a hook for potential clients. Designs should use the colors uploaded and can incorporate other colors to supplement the ones attached. The design should communicate professionalism, design, quality, and competence. Tagline can be used, but not required. Alternatively, a new one created. Current tagline is "Faster Insight, More Engagement"

I would like for the two sides to be contrasting. If the front is colored, the back should be white (or light vs dark colors).

Old company website is here www.brambleforge.net

```html
<!DOCTYPE html>
<html lang="en">
<head>
<meta charset="utf-8">
<title>Bramble Forge — Business Card</title>
<link rel="stylesheet" href="https://fonts.googleapis.com/css2?family=Montserrat:wght@400;500;700&display=swap">
<style>
  :root {
    --backdrop: #3a3a3a;
    --paper: #fbfbfa;
    --ink: #2e2b2b;
    --ink-soft: #4a4747;
    --rule: #6b6b6b;
    --accent: #f28c1c;
    --card-dark: #141414;
    --card-dark-2: #262626;
  }
  * { box-sizing: border-box; margin: 0; padding: 0; }
  html, body {
    width: 1200px; height: 801px; overflow: hidden;
    background: var(--backdrop);
    font-family: "Montserrat", sans-serif;
  }
  .stage {
    width: 1200px; height: 801px;
    display: flex; align-items: center; justify-content: center; gap: 40px;
  }
  .card {
    position: relative;
    width: 540px; height: 310px;
    border-bottom: 3px solid var(--accent);
    box-shadow: 0 10px 30px rgba(0,0,0,.35);
  }
  .card--front { background: var(--paper); }

  .brand-frame {
    position: absolute; left: 44px; top: 98px;
    width: 206px; height: 118px;
    border: 1px solid var(--accent);
    display: flex; align-items: center; justify-content: center;
  }
  .brand-name {
    font-weight: 500; font-size: 24px; letter-spacing: 1px;
    color: var(--ink);
  }
  .divider {
    position: absolute; left: 282px; top: 86px;
    width: 1px; height: 142px; background: var(--rule);
  }
  .contact {
    position: absolute; left: 304px; top: 84px;
    color: var(--ink-soft);
  }
  .contact__name {
    font-weight: 700; font-size: 17px; letter-spacing: .5px;
    color: var(--ink); text-transform: uppercase;
  }
  .contact__role {
    font-size: 13px; color: var(--accent); margin-top: 2px;
  }
  .contact__address {
    font-size: 12.5px; line-height: 1.45; margin-top: 12px;
  }
  .contact__lines { list-style: none; margin-top: 10px; }
  .contact__lines li {
    display: flex; align-items: center; gap: 7px;
    font-size: 12.5px; line-height: 1.55;
  }
  .contact__lines svg { width: 11px; height: 11px; flex: none; }

  .card--back { background: var(--card-dark); overflow: hidden; }
  .back-texture {
    position: absolute; inset: 0;
    background: linear-gradient(135deg, var(--card-dark) 0%, var(--card-dark-2) 55%, var(--card-dark) 100%);
  }
  .back-mark {
    position: absolute; right: 120px; top: 118px;
    font-weight: 500; font-size: 16px; letter-spacing: 1px;
    color: var(--accent);
  }
</style>
</head>
<body>
<main class="stage">
  <section class="card card--front">
    <div class="brand-frame"><span class="brand-name">Bramble Forge</span></div>
    <div class="divider"></div>
    <div class="contact">
      <p class="contact__name">Daniel Harlow</p>
      <p class="contact__role">President</p>
      <p class="contact__address">4820 Alder Creek Road<br>Fairview, VA 20117</p>
      <ul class="contact__lines">
        <li>
          <svg viewBox="0 0 12 12" aria-hidden="true"><circle cx="6" cy="6" r="6" fill="var(--accent)"/><path d="M4 3.2c.4-.3.8 0 1 .5l.3.7-.6.5c.3.7.8 1.2 1.4 1.5l.5-.6.7.3c.5.2.8.6.5 1-.6.8-1.6.6-2.6-.2S3.2 4 4 3.2z" fill="#fff"/></svg>
          571.555.0148
        </li>
        <li>
          <svg viewBox="0 0 12 12" aria-hidden="true"><circle cx="6" cy="6" r="6" fill="var(--accent)"/><rect x="3" y="4" width="6" height="4.2" fill="#fff"/><path d="M3 4l3 2.3L9 4" fill="none" stroke="var(--accent)" stroke-width=".8"/></svg>
          daniel@brambleforge.com
        </li>
        <li>
          <svg viewBox="0 0 12 12" aria-hidden="true"><circle cx="6" cy="6" r="6" fill="var(--accent)"/><circle cx="6" cy="6" r="3.2" fill="none" stroke="#fff" stroke-width=".8"/><path d="M2.8 6h6.4M6 2.8c-1.4 1.8-1.4 4.6 0 6.4M6 2.8c1.4 1.8 1.4 4.6 0 6.4" fill="none" stroke="#fff" stroke-width=".7"/></svg>
          www.brambleforge.net
        </li>
      </ul>
    </div>
  </section>

  <section class="card card--back">
    <div class="back-texture" role="img" aria-label="Tonal repeating brand pattern in dark greys"></div>
    <span class="back-mark">Bramble Forge</span>
  </section>
</main>
</body>
</html>
```